Kelmora Legal Business Card

I require a corporate business card for a new legal services business.

I do not have a logo, nor do I want one.

I require a clean, neat a professional card for a law firm.

Details:

Business Name: Kelmora Legal
Name: Debra Lindqvist
Title: Corporate Services Manager
Location: Office 14 (Top Floor), Toravel Business Centre, Quinlan Grove Street, Alotau CBD, Milne Bay Province.
Postal Address: PO Box 593, Alotau, 211, Milne Bay Province, Papua New Guinea.
Contact: T: +675 6418250, F: +675 6413362, M: +675 72915867, E: dlindqvist@kelmoraexample.com.pg.

I look forward to your design submissions.

Industry/Entity Type

Legal

```html
<!DOCTYPE html>
<html lang="en">
<head>
<meta charset="utf-8">
<title>Kelmora Legal Business Card</title>
<link rel="stylesheet" href="https://fonts.googleapis.com/css2?family=Exo+2:wght@400;500;600&display=swap">
<style>
  :root {
    --backdrop: #b9bec8;
    --card: #ffffff;
    --card-shade: #e9eaec;
    --ink: #3a3a3c;
    --brand: #2b5fb8;
    --blue-light: #0a92d8;
    --blue-deep: #33399a;
    --swoosh: #1c1c1e;
    --white: #ffffff;
  }
  * { margin: 0; padding: 0; box-sizing: border-box; }
  html, body { width: 1200px; height: 866px; overflow: hidden; }
  body {
    background: var(--backdrop);
    font-family: "Exo 2", sans-serif;
    display: flex;
    align-items: center;
    justify-content: center;
    gap: 50px;
  }
  .card {
    position: relative;
    width: 540px;
    height: 309px;
    background: radial-gradient(circle at 45% 45%, var(--card) 30%, var(--card-shade) 100%);
    box-shadow: 0 6px 18px rgba(0, 0, 0, 0.18);
    overflow: hidden;
  }
  .wordmark {
    font-weight: 500;
    color: var(--brand);
    letter-spacing: 0.5px;
    white-space: nowrap;
    line-height: 1.2;
  }
  .card-front { display: flex; align-items: center; justify-content: center; }
  .card-front .wordmark { font-size: 52px; }

  .card-back .swoosh { position: absolute; inset: 0; width: 100%; height: 100%; }
  .card-back .wordmark { position: absolute; left: 28px; top: 96px; font-size: 36px; }
  .holder { position: absolute; right: 26px; top: 22px; text-align: right; color: var(--ink); }
  .holder-name { font-size: 19px; font-weight: 500; letter-spacing: 1px; text-transform: uppercase; }
  .holder-title { font-size: 13px; }
  .contact-list {
    position: absolute; left: 22px; bottom: 12px;
    list-style: none; color: var(--white); font-size: 11px; line-height: 17px;
  }
  .contact-list li { display: flex; align-items: center; gap: 8px; }
  .contact-list svg { width: 10px; height: 10px; fill: var(--white); }
  .office {
    position: absolute; right: 24px; top: 165px;
    text-align: right; color: var(--white); font-size: 12.5px; line-height: 17px;
  }
  .website {
    position: absolute; right: 24px; top: 228px;
    color: var(--white); font-size: 12.5px;
  }
</style>
</head>
<body>
  <section class="card card-front">
    <div class="wordmark">Kelmora Legal</div>
  </section>

  <section class="card card-back">
    <svg class="swoosh" viewBox="0 0 540 309" preserveAspectRatio="none" aria-hidden="true">
      <defs>
        <radialGradient id="band-fill" cx="62%" cy="68%" r="60%">
          <stop offset="0" stop-color="var(--blue-light)"/>
          <stop offset="1" stop-color="var(--blue-deep)"/>
        </radialGradient>
      </defs>
      <path d="M0,215 C150,200 330,130 540,115 L540,309 L0,309 Z" fill="url(#band-fill)"/>
      <path d="M0,203 C150,186 310,118 470,98 C320,128 160,198 0,222 Z" fill="var(--swoosh)"/>
    </svg>

    <div class="wordmark">Kelmora Legal</div>

    <div class="holder">
      <p class="holder-name">Rowan Ashby</p>
      <p class="holder-title">Managing Director</p>
    </div>

    <ul class="contact-list">
      <li><svg viewBox="0 0 12 12"><path d="M2 1l2 0 1 3-1.5 1a6 6 0 0 0 3.5 3.5L8 7l3 1 0 2c-5 1-10-4-9-9z"/></svg>012 345 6789</li>
      <li><svg viewBox="0 0 12 12"><path d="M3 0h6v12H3z M4 1v9h4V1z"/></svg>012 345 6789</li>
      <li><svg viewBox="0 0 12 12"><path d="M3 0h5v3H3z M1 4h10v6H1z M3 6h6v1H3z"/></svg>012 345 6789</li>
      <li><svg viewBox="0 0 12 12"><path d="M0 2h12v8H0z M1 3l5 4 5-4" stroke="#33399a" stroke-width="0.8"/></svg>urname@email.com</li>
    </ul>

    <p class="office">047.12th floor,Mall<br>Harbour Road LKG</p>
    <p class="website">www.urwebsitename.com</p>
  </section>
</body>
</html>
```